Maple Lantern Business Card

Design of business cards

Target Market(s)

We are aiming as small business owners who need anything from basic business structures, website plans, business processes and quality assurance.

Industry/Entity Type

Business

Colors

Designer to choose colors to be used in the design.

Requirements
Nice to have
• I would prefer one side of the card to use the green from the logo. Prefer to have the same font as the logo.

```html
<!DOCTYPE html>
<html lang="en">
<head>
<meta charset="utf-8">
<title>Maple Lantern Business Card</title>
<link rel="stylesheet" href="https://fonts.googleapis.com/css2?family=Ubuntu:wght@400;500&display=swap">
<style>
  :root {
    --stage: #ece9e4;
    --card: #ffffff;
    --card-tint: #f1f1f1;
    --ink: #2b2b2b;
    --ink-soft: #4a4a4a;
    --brand-green: #8cc63f;
    --icon-dark: #1e1e1e;
    --icon-red: #e8334f;
    --warm-1: #f0a03a;
    --warm-2: #e6cf55;
    --warm-3: #8fcf7a;
    --warm-4: #4fc0a0;
    --cool-1: #e0254f;
    --cool-2: #e65a7c;
    --cool-3: #8a5a86;
    --cool-4: #2f5f78;
  }
  * { box-sizing: border-box; margin: 0; padding: 0; }
  html, body { width: 1200px; height: 804px; overflow: hidden; }
  body {
    background: var(--stage);
    font-family: "Ubuntu", sans-serif;
    color: var(--ink);
    position: relative;
  }
  .card {
    position: absolute;
    top: 122px;
    width: 330px;
    height: 560px;
    background: var(--card);
    border-radius: 4px;
    box-shadow: 0 6px 18px rgba(0,0,0,0.14);
    overflow: hidden;
  }
  .card--front { left: 225px; }
  .card--back { left: 645px; }

  /* Front */
  .front-pattern {
    position: absolute;
    left: 0;
    width: 100%;
  }
  .front-pattern--top {
    top: 0;
    height: 210px;
    background: linear-gradient(110deg, var(--warm-1) 0%, var(--warm-2) 40%, var(--warm-3) 72%, var(--warm-4) 100%);
  }
  .front-pattern--bottom {
    bottom: 0;
    height: 258px;
    background: linear-gradient(160deg, var(--cool-1) 0%, var(--cool-2) 45%, var(--cool-3) 78%, var(--cool-4) 100%);
  }
  .front-band {
    position: absolute;
    top: 210px;
    left: 0;
    width: 100%;
    height: 92px;
    background: linear-gradient(100deg, var(--card) 55%, var(--card-tint) 100%);
    display: flex;
    align-items: center;
    padding-left: 60px;
  }
  .front-url {
    font-size: 21px;
    font-weight: 400;
    color: var(--ink);
    letter-spacing: 0.2px;
  }

  /* Back */
  .back-pattern {
    position: absolute;
    inset: 0;
    width: 100%;
    height: 100%;
  }
  .brand {
    position: absolute;
    top: 44px;
    left: 34px;
    display: flex;
    align-items: center;
    gap: 10px;
  }
  .brand-mark {
    width: 14px;
    height: 14px;
    background: var(--brand-green);
  }
  .brand-name {
    font-size: 15px;
    font-weight: 500;
    color: var(--brand-green);
    line-height: 1.15;
    text-transform: uppercase;
    letter-spacing: 0.6px;
  }
  .contact-list { list-style: none; }
  .contact {
    position: absolute;
    display: flex;
    align-items: center;
    gap: 14px;
    font-size: 13px;
    color: var(--ink-soft);
  }
  .contact--name { top: 200px; left: 46px; font-size: 14px; color: var(--ink); text-transform: uppercase; }
  .contact--email { top: 246px; left: 72px; }
  .contact--phone { top: 292px; left: 98px; }
  .contact--chat { top: 338px; left: 124px; text-transform: uppercase; font-size: 12.5px; }
  .contact-icon {
    width: 30px;
    height: 30px;
    border-radius: 50%;
    display: flex;
    align-items: center;
    justify-content: center;
    flex: none;
  }
  .contact-icon--green { background: var(--brand-green); }
  .contact-icon--dark { background: var(--icon-dark); }
  .contact-icon--red { background: var(--icon-red); }
  .contact-icon svg { width: 16px; height: 16px; }
</style>
</head>
<body>

<section class="card card--front" aria-label="Card front">
  <div class="front-pattern front-pattern--top" role="img" aria-label="Warm geometric triangle pattern in orange, yellow and green"></div>
  <div class="front-band">
    <p class="front-url">www.maplelantern.co</p>
  </div>
  <div class="front-pattern front-pattern--bottom" role="img" aria-label="Geometric triangle pattern in red, pink, purple and teal"></div>
</section>

<section class="card card--back" aria-label="Card back">
  <svg class="back-pattern" viewBox="0 0 330 560" preserveAspectRatio="none" role="img" aria-label="Diagonal geometric triangle pattern, green at top right and pink at bottom left">
    <defs>
      <linearGradient id="greenBand" x1="0" y1="0" x2="1" y2="1">
        <stop offset="0" stop-color="#c9d87a"/>
        <stop offset="0.5" stop-color="#74c68a"/>
        <stop offset="1" stop-color="#4a8f62"/>
      </linearGradient>
      <linearGradient id="pinkBand" x1="0" y1="0" x2="1" y2="1">
        <stop offset="0" stop-color="#e0254f"/>
        <stop offset="1" stop-color="#ee7a93"/>
      </linearGradient>
      <linearGradient id="paper" x1="0" y1="0" x2="1" y2="1">
        <stop offset="0" stop-color="#ffffff"/>
        <stop offset="1" stop-color="#e9e9e9"/>
      </linearGradient>
    </defs>
    <rect width="330" height="560" fill="url(#paper)"/>
    <polygon points="185,0 330,0 330,300" fill="url(#greenBand)"/>
    <polygon points="0,320 0,560 160,560" fill="url(#pinkBand)"/>
  </svg>

  <div class="brand">
    <span class="brand-mark"></span>
    <span class="brand-name">Maple Lantern<br>Consulting</span>
  </div>

  <ul class="contact-list">
    <li class="contact contact--name">
      <span class="contact-icon contact-icon--green">
        <svg viewBox="0 0 16 16"><circle cx="8" cy="5.5" r="3" fill="#fff"/><path d="M2.5 14c0-3 2.5-5 5.5-5s5.5 2 5.5 5z" fill="#fff"/></svg>
      </span>
      Your Name Here
    </li>
    <li class="contact contact--email">
      <span class="contact-icon contact-icon--dark">
        <svg viewBox="0 0 16 16"><rect x="2" y="4" width="12" height="8" fill="none" stroke="#fff" stroke-width="1.4"/><path d="M2 4l6 5 6-5" fill="none" stroke="#fff" stroke-width="1.4"/></svg>
      </span>
      hello@maplelantern.co
    </li>
    <li class="contact contact--phone">
      <span class="contact-icon contact-icon--red">
        <svg viewBox="0 0 16 16"><path d="M4 2.5l2.2 0 1 3-1.5 1.2c.8 1.6 2 2.8 3.6 3.6L10.5 8.8l3 1v2.2c0 .8-.7 1.5-1.5 1.5C6.8 13.5 2.5 9.2 2.5 4c0-.8.7-1.5 1.5-1.5z" fill="#fff"/></svg>
      </span>
      +104455201783
    </li>
    <li class="contact contact--chat">
      <span class="contact-icon contact-icon--dark">
        <svg viewBox="0 0 16 16"><rect x="3" y="4" width="10" height="7" rx="1.5" fill="none" stroke="#fff" stroke-width="1.4"/><path d="M6 11l-1.5 2.5L8.5 11" fill="#fff"/></svg>
      </span>
      Your Chat Handle
    </li>
  </ul>
</section>

</body>
</html>
```